Dental Practice Billboard Design

We are a newer dental practice in need of a simple but appealing billboard for our growing dental practice to attract new patients. The practice is owned by husband and wife dentists and is family friendly in a small town in Kentucky. We try to be very friendly and caring to our patients. Would prefer a blue background for the billboard and our tooth logo to be prominent. We are partial to the Patua One font used in the image below but please feel free to tweak it as you deem necessary. The shape of the uppercase D and lowercase g are why we like that font, so fonts with a similarly shaped “D” and “g” would work as well. Please include our phone number (606) 847-3962. Please see our website Harlowfamilydentistry.com for more info on the practice if needed. Thank you! Looking forward to seeing your creation.
Updates

The dimensions will be 12ft x 24ft (3.6576m x 7.3152m). Apologies for not including this in the original prompt. Thank you all for your submissions.

Industry/Entity Type

Dental

Font styles to use
Other font styles liked:
• Patua One

Colors
0054AA
0677BA
7BADD7
CADEEF
E8F1F8
0094D4
00A9DD
6FCCEA
C7EBF8
E9F6FB
00AB8E
00BBA5
67D7C9
C6EFE9
E9F9F6
59FF00
82FF00
B8FF75
E3FFCB
F4FFEA

Requirements
Must have
• Phone number, website, Logo, Practice name “Harlow Family Dentistry”
Should not have
• A tagline or slogan

```html
<!DOCTYPE html>
<html lang="en">
<head>
<meta charset="utf-8">
<title>Harlow Family Dentistry Billboard</title>
<link rel="stylesheet" href="https://fonts.googleapis.com/css2?family=Bitter:wght@600;700&family=Montserrat:wght@500;700&family=Fira+Sans+Condensed:wght@600&display=swap">
<style>
  :root {
    --blue-deep: #0048a0;
    --blue-main: #0054AA;
    --blue-light: #0a66c6;
    --green: #22b814;
    --green-text: #2fc11f;
    --white: #ffffff;
    --text-soft: #f1f5fa;
    --page: #ffffff;
    --photo-a: #7fa9cf;
    --photo-b: #b5463f;
  }
  * { box-sizing: border-box; margin: 0; padding: 0; }
  html, body {
    width: 1097px; height: 1200px; overflow: hidden;
    background: var(--page);
  }
  .billboard {
    position: absolute;
    left: 40px; top: 346px;
    width: 1017px; height: 508px;
    overflow: hidden;
    background: radial-gradient(ellipse at 70% 20%, var(--blue-light) 0%, var(--blue-main) 45%, var(--blue-deep) 100%);
    color: var(--white);
    font-family: "Bitter", Georgia, serif;
  }
  .brand {
    position: absolute; left: 58px; top: 50px;
    display: flex; align-items: center; gap: 14px;
  }
  .brand-dot {
    width: 72px; height: 72px; border-radius: 50%;
    background: var(--green);
    flex: none;
  }
  .brand-name {
    font-weight: 700; font-size: 31px; line-height: 36px;
    color: var(--text-soft);
  }
  .family-photo {
    position: absolute; left: 428px; top: 46px;
    width: 226px; height: 462px;
    border-radius: 110px 110px 0 0;
    background: linear-gradient(180deg, var(--photo-a) 0%, #9bbbd8 45%, var(--photo-b) 70%, #2d4a78 100%);
    opacity: 0.85;
  }
  .headline {
    position: absolute; left: 45px; top: 184px;
    font-weight: 700; font-size: 40px; line-height: 44px;
    color: var(--text-soft);
  }
  .subline {
    position: absolute; left: 46px; top: 324px;
    font-family: "Montserrat", Arial, sans-serif; font-weight: 500;
    font-size: 25px; color: var(--text-soft);
  }
  .tech-pill {
    position: absolute; left: 45px; top: 361px;
    width: 329px; height: 44px; border-radius: 22px;
    background: var(--green);
    font-family: "Montserrat", Arial, sans-serif; font-weight: 700;
    font-size: 24px; line-height: 44px; text-align: center;
  }
  .website {
    position: absolute; left: 45px; top: 424px;
    font-weight: 700; font-size: 28px; color: var(--text-soft);
    white-space: nowrap;
  }
  .services-title {
    position: absolute; left: 688px; top: 56px;
    font-weight: 700; font-size: 27px; line-height: 30px;
    text-transform: uppercase; color: var(--text-soft);
  }
  .services-list {
    position: absolute; left: 693px; top: 128px;
    display: grid; grid-template-columns: 150px 152px;
    row-gap: 7px; list-style: none;
    font-weight: 600; font-size: 17px; line-height: 20px;
  }
  .services-list li { display: flex; align-items: center; gap: 9px; white-space: nowrap; }
  .services-list li::before {
    content: ""; width: 10px; height: 10px; border-radius: 50%;
    background: var(--green-text); flex: none;
  }
  .insurance {
    position: absolute; left: 666px; top: 309px;
    font-weight: 700; font-size: 27px; line-height: 29px;
    text-transform: uppercase; white-space: nowrap;
  }
  .insurance .highlight { color: var(--green-text); display: block; }
  .phone {
    position: absolute; left: 662px; top: 412px;
    font-family: "Fira Sans Condensed", Arial, sans-serif; font-weight: 600;
    font-size: 52px; line-height: 60px; color: var(--text-soft);
    white-space: nowrap;
  }
</style>
</head>
<body>
  <main class="billboard">
    <div class="family-photo" role="img" aria-label="Photo of a smiling family of mother, father and daughter pointing toward the text"></div>

    <div class="brand">
      <span class="brand-dot"></span>
      <div class="brand-name">Harlow<br>Family Dentistry</div>
    </div>

    <h1 class="headline">Comprehensive<br>Dental Care<br>for your Family</h1>
    <p class="subline">with Modern Care &amp;</p>
    <div class="tech-pill">Advanced Technology</div>
    <p class="website">harlowfamilydentistry.com</p>

    <h2 class="services-title">Services that will<br>make you smile</h2>
    <ul class="services-list">
      <li>Crowns</li><li>Veneers</li>
      <li>Root Canals</li><li>Whitening</li>
      <li>Extractions</li><li>Fillings</li>
      <li>Implants</li><li>Cleanings</li>
      <li>Bridges</li><li>Dentures</li>
      <li>Clear Aligners</li><li>Overdentures</li>
    </ul>

    <p class="insurance">We accept most<span class="highlight">Major dental<br>insurance providers</span></p>
    <p class="phone">(606) 847-3962</p>
  </main>
</body>
</html>
```